Computer repair services flyer

This flyer / leaflet is required to promote my local computer and laptop repair business. It will primarily be used for pinning to notice boards when I get access to shared accommodation but I will also use it in the future for posting through letterboxes in affluent areas.

Company branding, logo, services, pricing, contact details etc. can be found on my website at : www.brightlanetech.co.uk

The services I would predominantly like to promote on this flyer are :

Speeding up slow / old computers
Virus removal
Lost data recovered
Broken laptop screen replacements
Dead laptops fixed
We buy and recycle broken laptops for cash

Other features to highlight :

Friendly and experienced
We are local (Near to Cardiff city center)
Quick repair turnaround - most repairs within 24hours
Affordable / No VAT
Free diagnostics
No Fix = No fee
Free collection and delivery
We Guarantee our work

Calls to action and attention grabbing if possible. Offer 10% off. Free cooling fan clean.

Size of flyer = A5 (210 x 148mm or 8.3 x 5.8in) portrait, single sided colour.

Target Market(s)

18 to 60 years

Industry/Entity Type

Accommodation

Requirements
Must have
• 02940 613857

```html
<!DOCTYPE html>
<html lang="en">
<head>
<meta charset="utf-8">
<title>Bright Lane Tech – Computer Repair Flyer</title>
<link rel="stylesheet" href="https://fonts.googleapis.com/css2?family=Roboto:wght@400;700;900&display=swap">
<style>
  :root {
    --orange: #f27a1a;
    --orange-deep: #e0650c;
    --black: #111111;
    --white: #ffffff;
    --ink: #1a1a1a;
    --grey: #9a9a9a;
    --photo-blue: #4f7fa8;
  }
  * { box-sizing: border-box; margin: 0; padding: 0; }
  html, body { width: 845px; height: 1200px; overflow: hidden; background: var(--white); }
  body { font-family: "Roboto", Arial, sans-serif; color: var(--ink); }
  .flyer { position: relative; width: 845px; height: 1200px; overflow: hidden; background: var(--white); }
  .block { position: absolute; }

  .photo-team { left: 0; top: 0; width: 544px; height: 262px;
    background: linear-gradient(135deg, #e9eef3 0%, #b9c9d8 45%, #3f5f80 100%); }
  .brand { left: 544px; top: 0; width: 301px; height: 161px; display: flex; align-items: center; justify-content: center; gap: 12px; }
  .brand-mark { width: 22px; height: 22px; background: var(--orange); flex: none; }
  .brand-name { font-weight: 900; font-size: 34px; line-height: 1; color: var(--black); letter-spacing: -0.5px; }
  .call { left: 544px; top: 161px; width: 301px; height: 101px; background: var(--orange); color: var(--white); padding: 16px 0 0 28px; }
  .call-label { font-weight: 700; font-size: 36px; line-height: 1; }
  .call-number { font-weight: 700; font-size: 36px; line-height: 1.2; margin-top: 4px; }

  .price { left: 0; top: 262px; width: 307px; height: 151px; background: var(--black); color: var(--white); display: flex; align-items: center; padding-left: 20px; gap: 12px; }
  .price-label { font-weight: 900; font-size: 30px; line-height: 1.05; }
  .price-value { font-weight: 900; font-size: 78px; color: var(--orange); line-height: 1; letter-spacing: -2px; }

  .photo-keyboard { left: 307px; top: 262px; width: 289px; height: 339px;
    background: linear-gradient(160deg, #c9d9ea 0%, #6f96bd 50%, #2d4f78 100%); border-left: 4px solid var(--white); }
  .photo-drive { left: 596px; top: 262px; width: 249px; height: 339px;
    background: linear-gradient(200deg, #d8dee6 0%, #8a9bb0 55%, #3a4656 100%); border-left: 4px solid var(--white); }

  .services { left: 0; top: 413px; width: 307px; height: 555px; background: var(--orange); color: var(--white); padding: 28px 0 0 24px; }
  .services-title { font-weight: 900; font-size: 33px; margin-bottom: 20px; }
  .service-list { list-style: none; }
  .service-list li { position: relative; font-weight: 700; font-size: 25px; line-height: 1.22; padding-left: 34px; margin-bottom: 15px; }
  .service-list li::before { content: ""; position: absolute; left: 2px; top: 6px; width: 14px; height: 14px; border: 3px solid var(--white); border-radius: 50%; }

  .features { left: 307px; top: 601px; width: 538px; height: 367px; padding: 14px 0 0 18px; }
  .feature-list { list-style: none; }
  .feature-list li { display: flex; align-items: flex-start; gap: 10px; font-weight: 700; font-size: 25px; line-height: 1.2; margin-bottom: 7px; color: var(--black); }
  .feature-list svg { flex: none; margin-top: 2px; }

  .offer { left: 0; top: 968px; width: 845px; height: 42px; background: var(--black); color: var(--white); font-size: 26px; text-align: center; line-height: 42px; }

  .map { left: 0; top: 1010px; width: 270px; height: 190px;
    background: linear-gradient(135deg, #f1efe8 0%, #e4e2d8 60%, #d9e3d0 100%); }
  .contact { left: 290px; top: 1030px; width: 290px; }
  .contact-item { position: relative; padding-left: 24px; font-weight: 700; font-size: 19px; line-height: 1.3; margin-bottom: 22px; }
  .contact-item::before { content: ""; position: absolute; left: 0; top: 5px; width: 11px; height: 11px; background: var(--orange); }
  .contact-item.tight { margin-bottom: 4px; }
  .social { left: 590px; top: 1022px; width: 255px; list-style: none; }
  .social li { display: flex; align-items: center; gap: 12px; font-weight: 700; font-size: 17px; height: 42px; }
  .social-box { width: 26px; height: 26px; background: var(--grey); flex: none; }
</style>
</head>
<body>
<main class="flyer">
  <div class="block photo-team" role="img" aria-label="Photo of three smiling office workers giving thumbs up at a computer"></div>

  <header class="block brand">
    <span class="brand-mark"></span>
    <span class="brand-name">Bright Lane Tech</span>
  </header>

  <section class="block call">
    <p class="call-label">Call Now</p>
    <p class="call-number">02940 613857</p>
  </section>

  <section class="block price">
    <p class="price-label">PRICES<br>START<br>FROM</p>
    <p class="price-value">£19</p>
  </section>

  <div class="block photo-keyboard" role="img" aria-label="Photo of a stethoscope resting on a computer keyboard"></div>
  <div class="block photo-drive" role="img" aria-label="Photo of a hand holding an open hard drive"></div>

  <section class="block services">
    <h2 class="services-title">OUR SERVICES</h2>
    <ul class="service-list">
      <li>Speeding up slow / old computers</li>
      <li>Virus removal</li>
      <li>Lost data recovered</li>
      <li>Broken laptop screen replacements</li>
      <li>Dead laptops fixed</li>
      <li>We buy and recycle broken laptops for cash</li>
    </ul>
  </section>

  <section class="block features">
    <ul class="feature-list">
      <li><svg width="24" height="24" viewBox="0 0 24 24"><path d="M3 13l6 6L21 4" fill="none" stroke="#f27a1a" stroke-width="4" stroke-linecap="round" stroke-linejoin="round"/></svg>Friendly and experienced</li>
      <li><svg width="24" height="24" viewBox="0 0 24 24"><path d="M3 13l6 6L21 4" fill="none" stroke="#f27a1a" stroke-width="4" stroke-linecap="round" stroke-linejoin="round"/></svg>We are local (Near to Cardiff<br>city center)</li>
      <li><svg width="24" height="24" viewBox="0 0 24 24"><path d="M3 13l6 6L21 4" fill="none" stroke="#f27a1a" stroke-width="4" stroke-linecap="round" stroke-linejoin="round"/></svg>Quick repair turnaround -<br>most repairs within 24hours</li>
      <li><svg width="24" height="24" viewBox="0 0 24 24"><path d="M3 13l6 6L21 4" fill="none" stroke="#f27a1a" stroke-width="4" stroke-linecap="round" stroke-linejoin="round"/></svg>Affordable / No VAT</li>
      <li><svg width="24" height="24" viewBox="0 0 24 24"><path d="M3 13l6 6L21 4" fill="none" stroke="#f27a1a" stroke-width="4" stroke-linecap="round" stroke-linejoin="round"/></svg>Free diagnostics</li>
      <li><svg width="24" height="24" viewBox="0 0 24 24"><path d="M3 13l6 6L21 4" fill="none" stroke="#f27a1a" stroke-width="4" stroke-linecap="round" stroke-linejoin="round"/></svg>No Fix = No Fees</li>
      <li><svg width="24" height="24" viewBox="0 0 24 24"><path d="M3 13l6 6L21 4" fill="none" stroke="#f27a1a" stroke-width="4" stroke-linecap="round" stroke-linejoin="round"/></svg>Free collection and delivery</li>
      <li><svg width="24" height="24" viewBox="0 0 24 24"><path d="M3 13l6 6L21 4" fill="none" stroke="#f27a1a" stroke-width="4" stroke-linecap="round" stroke-linejoin="round"/></svg>We Guarantee our work</li>
    </ul>
  </section>

  <p class="block offer">Offer 10% off. Free cooling fan clean.</p>

  <div class="block map" role="img" aria-label="Street map of Cardiff and surrounding areas"></div>

  <address class="block contact" style="font-style: normal;">
    <p class="contact-item">14 Harrow Street,<br>Llanishen<br>Cardiff&nbsp; CF14 9QD</p>
    <p class="contact-item tight">hello@brightlanetech.co.uk</p>
    <p class="contact-item tight">www.brightlanetech.co.uk</p>
  </address>

  <ul class="block social">
    <li><span class="social-box"></span>brightlanetech.co.uk</li>
    <li><span class="social-box"></span>brightlanetech.co.uk</li>
    <li><span class="social-box"></span>brightlanetech.co.uk</li>
    <li><span class="social-box"></span>brightlanetech.co.uk</li>
  </ul>
</main>
</body>
</html>
```